Tilda Tinkerwire, An IT Company Has New Logo, Need Fresh Business Cards

IT company is called Tilda Tinkerwire and is displayed nicely with the new logo from here on pitchloft. Would like a fresh business card look that encompasses the idea that we want clients to Cherish Every Gadget. I love the use of circuitry with hearts as endpoints and x's and o's. It needs to have room for my certification logos of which there are 4 and a BRJ Alumni log. I am attaching my current card to illustrate how it has always captured attention, but that was in the early stages of business when I was doing more residential work. I am focused on businesses now, so a level of professionalism is necessary. I would also like the card to lend itself well to additional stationary, email signature, ticketing template for my workboard, etc. For the time being, I need the card for an upcoming conference so that work will come later. Color scheme should be that of the new logo. Thank you and I look forward to the designs.

Target Market(s)

Businesses looking for IT services.

Industry/Entity Type

Information Technology

Contact Information for Business Card

See above

Requirements
Must have
• New logo colors and a warm feel. Possibly a tad feminine as I am female, but appealing to males.
Nice to have
• I would like techy, but no too much so. I like friendly and connecting feels. People LOVED my old card and called me because it gave them a warm feeling.

```html
<!DOCTYPE html>
<html lang="en">
<head>
<meta charset="utf-8">
<title>Tilda Tinkerwire – Business Card</title>
<link rel="stylesheet" href="https://fonts.googleapis.com/css2?family=Quicksand:wght@500;700&family=Noto+Sans:wght@400&display=swap">
<style>
  :root {
    --page: #ffffff;
    --board: #cccccc;
    --card-lilac: #d4b2d6;
    --card-white: #ffffff;
    --ink-purple: #7f0f86;
    --pill-purple: #7d0a82;
    --logo-blue: #86c9dc;
    --tag-pink: #d79ac4;
    --rule: #bdbdbd;
  }
  html, body {
    margin: 0;
    padding: 0;
    width: 1052px;
    height: 1200px;
    overflow: hidden;
    background: var(--page);
  }
  .canvas {
    position: relative;
    width: 1052px;
    height: 1200px;
  }
  .board {
    position: absolute;
    left: 3px;
    top: 3px;
    width: 1045px;
    height: 1104px;
    background: var(--board);
    border-radius: 10px;
  }
  .guide-line {
    position: absolute;
    left: 816px;
    top: 968px;
    width: 1px;
    height: 230px;
    background: var(--rule);
  }
  .card {
    position: absolute;
    left: 197px;
    width: 654px;
    height: 373px;
    display: block;
  }
  .card--front { top: 177px; }
  .card--alt { top: 595px; }
  .brand-name {
    font-family: "Quicksand", sans-serif;
    font-weight: 700;
    font-size: 24px;
    fill: var(--logo-blue);
  }
  .brand-tagline {
    font-family: "Quicksand", sans-serif;
    font-weight: 700;
    font-size: 8.5px;
    letter-spacing: 2.6px;
    fill: var(--tag-pink);
  }
  .call-line {
    font-family: "Quicksand", sans-serif;
    font-weight: 700;
    font-size: 34px;
    letter-spacing: 1.5px;
    fill: var(--ink-purple);
  }
  .phone-line {
    font-family: "Noto Sans", sans-serif;
    font-size: 36px;
    letter-spacing: 1px;
    fill: var(--ink-purple);
  }
  .contact-line {
    font-family: "Noto Sans", sans-serif;
    font-size: 16.5px;
    fill: var(--ink-purple);
  }
  .badge-slot { fill: var(--pill-purple); }
  .badge-label {
    font-family: "Noto Sans", sans-serif;
    font-size: 16px;
    fill: #000000;
  }
</style>
</head>
<body>
<div class="canvas">
  <div class="board"></div>

  <!-- Card layout, first variant -->
  <svg class="card card--front" viewBox="0 0 654 373" xmlns="http://www.w3.org/2000/svg">
    <defs>
      <linearGradient id="art-fill-a" x1="0" y1="0" x2="1" y2="0">
        <stop offset="0" stop-color="#d4b2d6" stop-opacity="0"/>
        <stop offset="0.3" stop-color="#e2d6e3"/>
        <stop offset="0.75" stop-color="#e5dde6"/>
        <stop offset="1" stop-color="#d88f86"/>
      </linearGradient>
    </defs>
    <rect class="card-base" width="654" height="373" fill="var(--card-lilac)"/>
    <path class="header-arc" d="M0 0 H654 V30 C600 110 460 150 330 151 C150 152 20 95 0 0 Z" fill="var(--card-white)"/>
    <rect class="hero-art" x="440" y="25" width="214" height="348" fill="url(#art-fill-a)" role="img" aria-label="Illustration of a friendly technician hugging a desktop computer tower"/>
    <circle class="brand-mark" cx="333" cy="48" r="36" fill="none" stroke="var(--logo-blue)" stroke-width="3"/>
    <text class="brand-name" x="333" y="124" text-anchor="middle">Tilda Tinkerwire</text>
    <text class="brand-tagline" x="333" y="136" text-anchor="middle">CHERISH EVERY GADGET</text>
    <text class="call-line" x="442" y="199" text-anchor="end">CALL TILDA!</text>
    <text class="phone-line" x="439" y="240" text-anchor="end">407-555-0188</text>
    <g class="icon-globe" fill="none" stroke="var(--ink-purple)" stroke-width="1.5">
      <circle cx="33" cy="273" r="7"/>
      <ellipse cx="33" cy="273" rx="3" ry="7"/>
      <line x1="26" y1="273" x2="40" y2="273"/>
    </g>
    <text class="contact-line" x="50" y="275">www.tilda-tinkerwire.com</text>
    <g class="icon-mail">
      <rect x="26" y="292" width="15" height="10" fill="var(--ink-purple)"/>
      <path d="M26 292 L33.5 298 L41 292" fill="none" stroke="#d4b2d6" stroke-width="1.3"/>
    </g>
    <text class="contact-line" x="50" y="300">hello@tilda-tinkerwire.com</text>
    <g class="badge-row">
      <ellipse class="badge-slot" cx="58" cy="337" rx="39" ry="14.5"/>
      <text class="badge-label" x="58" y="343" text-anchor="middle">icon 1</text>
      <ellipse class="badge-slot" cx="153" cy="337" rx="39" ry="14.5"/>
      <text class="badge-label" x="153" y="343" text-anchor="middle">icon 2</text>
      <ellipse class="badge-slot" cx="245" cy="337" rx="39" ry="14.5"/>
      <text class="badge-label" x="245" y="343" text-anchor="middle">icon 3</text>
      <ellipse class="badge-slot" cx="337" cy="337" rx="39" ry="14.5"/>
      <text class="badge-label" x="337" y="343" text-anchor="middle">icon 4</text>
      <ellipse class="badge-slot" cx="424" cy="337" rx="39" ry="14.5"/>
      <text class="badge-label" x="424" y="343" text-anchor="middle">icon 5</text>
    </g>
  </svg>

  <!-- Card layout, second variant -->
  <svg class="card card--alt" viewBox="0 0 654 373" xmlns="http://www.w3.org/2000/svg">
    <defs>
      <linearGradient id="art-fill-b" x1="0" y1="0" x2="1" y2="0">
        <stop offset="0" stop-color="#d4b2d6" stop-opacity="0"/>
        <stop offset="0.3" stop-color="#e2d6e3"/>
        <stop offset="0.75" stop-color="#e5dde6"/>
        <stop offset="1" stop-color="#d88f86"/>
      </linearGradient>
      <linearGradient id="pattern-fill-b" x1="0" y1="0" x2="0" y2="1">
        <stop offset="0" stop-color="#dcc4de"/>
        <stop offset="1" stop-color="#d4b2d6"/>
      </linearGradient>
    </defs>
    <rect class="card-base" width="654" height="373" fill="var(--card-lilac)"/>
    <rect class="circuit-backdrop" x="0" y="60" width="520" height="313" fill="url(#pattern-fill-b)" role="img" aria-label="Faint circuit-trace background pattern"/>
    <path class="header-arc" d="M0 0 H654 V30 C600 110 460 150 330 151 C150 152 20 95 0 0 Z" fill="var(--card-white)"/>
    <rect class="hero-art" x="440" y="25" width="214" height="348" fill="url(#art-fill-b)" role="img" aria-label="Illustration of a friendly technician hugging a desktop computer tower"/>
    <circle class="brand-mark" cx="333" cy="48" r="36" fill="none" stroke="var(--logo-blue)" stroke-width="3"/>
    <text class="brand-name" x="333" y="124" text-anchor="middle">Tilda Tinkerwire</text>
    <text class="brand-tagline" x="333" y="136" text-anchor="middle">CHERISH EVERY GADGET</text>
    <text class="call-line" x="442" y="199" text-anchor="end">CALL TILDA!</text>
    <text class="phone-line" x="439" y="240" text-anchor="end">407-555-0188</text>
    <g class="icon-globe" fill="none" stroke="var(--ink-purple)" stroke-width="1.5">
      <circle cx="33" cy="273" r="7"/>
      <ellipse cx="33" cy="273" rx="3" ry="7"/>
      <line x1="26" y1="273" x2="40" y2="273"/>
    </g>
    <text class="contact-line" x="50" y="275">www.tilda-tinkerwire.com</text>
    <g class="icon-mail">
      <rect x="26" y="292" width="15" height="10" fill="var(--ink-purple)"/>
      <path d="M26 292 L33.5 298 L41 292" fill="none" stroke="#d4b2d6" stroke-width="1.3"/>
    </g>
    <text class="contact-line" x="50" y="300">hello@tilda-tinkerwire.com</text>
    <g class="badge-row">
      <ellipse class="badge-slot" cx="58" cy="337" rx="39" ry="14.5"/>
      <text class="badge-label" x="58" y="343" text-anchor="middle">icon 1</text>
      <ellipse class="badge-slot" cx="153" cy="337" rx="39" ry="14.5"/>
      <text class="badge-label" x="153" y="343" text-anchor="middle">icon 2</text>
      <ellipse class="badge-slot" cx="245" cy="337" rx="39" ry="14.5"/>
      <text class="badge-label" x="245" y="343" text-anchor="middle">icon 3</text>
      <ellipse class="badge-slot" cx="337" cy="337" rx="39" ry="14.5"/>
      <text class="badge-label" x="337" y="343" text-anchor="middle">icon 4</text>
      <ellipse class="badge-slot" cx="424" cy="337" rx="39" ry="14.5"/>
      <text class="badge-label" x="424" y="343" text-anchor="middle">icon 5</text>
    </g>
  </svg>

  <div class="guide-line"></div>
</div>
</body>
</html>
```